New world-class investment firm needs a business card design

We need a business card design for a new investment firm called 'Dalvin Soeurs & Company.' We acquire companies in the media sector and secure funding from conservative ultra, high-net worth individuals. We would like a black and white color design. We are seeking classic, elegant, and sophisticated designs. The final design should communicate financial safety, class, timelessness, and highly ethical. On the back of the business card, we would simply like the lion logo to be centered. I have attached a mock card, and variations on it are welcomed.
Industry/Entity Type
Conservative
Font styles to use
Other font styles liked:
- Garamond
Look and feel
Each slider illustrates characteristics of the customer's brand and the style your logo design should communicate.

```html
<!DOCTYPE html>
<html lang="en">
<head>
<meta charset="utf-8">
<title>Dalvin Soeurs &amp; Company — Business Card</title>
<link rel="stylesheet" href="https://fonts.googleapis.com/css2?family=Open+Sans:wght@400&display=swap">
<style>
  :root {
    --backdrop: #e9e7e4;
    --card-black: #1e1e1e;
    --silver-light: #e6e6e6;
    --silver-mid: #c9c9c9;
    --silver-dark: #a9a9a9;
    --ink-dark: #2a2a2a;
    --ink-light: #f4f4f4;
  }
  html, body {
    margin: 0;
    padding: 0;
    width: 1200px;
    height: 959px;
    overflow: hidden;
    background: var(--backdrop);
  }
  .canvas {
    position: relative;
    width: 1200px;
    height: 959px;
  }
  .card {
    position: absolute;
    left: 100px;
    top: 194px;
    width: 1000px;
    height: 571px;
    background: var(--card-black);
    box-shadow: 0 18px 40px rgba(0,0,0,0.28);
    overflow: hidden;
  }
  .top-strip {
    position: absolute;
    left: 0; right: 0; top: 0;
    height: 20px;
    display: flex;
    gap: 5px;
  }
  .top-strip span {
    flex: 1;
    background: linear-gradient(180deg, var(--silver-light), var(--silver-dark));
  }
  .firm-name {
    position: absolute;
    left: 0; right: 0; top: 88px;
    margin: 0;
    text-align: center;
    font-family: "Open Sans", Arial, sans-serif;
    font-weight: 400;
    font-size: 50px;
    line-height: 1.1;
    color: var(--ink-light);
  }
  .person {
    position: absolute;
    left: 0; right: 0; top: 218px;
    margin: 0;
    text-align: center;
    font-family: "Open Sans", Arial, sans-serif;
    font-weight: 400;
    color: var(--ink-light);
    text-transform: uppercase;
  }
  .person .name {
    display: block;
    font-size: 36px;
    letter-spacing: 0.5px;
  }
  .person .role {
    display: block;
    font-size: 24px;
    margin-top: 4px;
  }
  .contact-row {
    position: absolute;
    left: 22px; right: 22px;
    top: 332px;
    height: 218px;
    display: flex;
    gap: 10px;
  }
  .contact-box {
    flex: 1;
    background: linear-gradient(160deg, var(--silver-light) 0%, var(--silver-mid) 55%, var(--silver-dark) 100%);
    display: flex;
    flex-direction: column;
    align-items: center;
    justify-content: center;
    gap: 22px;
    font-family: "Open Sans", Arial, sans-serif;
    font-size: 19px;
    line-height: 1.45;
    color: var(--ink-dark);
    text-align: center;
  }
  .contact-icon {
    width: 50px;
    height: 50px;
  }
</style>
</head>
<body>
<main class="canvas">
  <article class="card">
    <div class="top-strip"><span></span><span></span><span></span></div>

    <h1 class="firm-name">Dalvin Soeurs &amp; Company</h1>

    <p class="person">
      <span class="name">Adrian Whitmore</span>
      <span class="role">General Manager</span>
    </p>

    <section class="contact-row">
      <div class="contact-box phone">
        <svg class="contact-icon" viewBox="0 0 50 50" aria-hidden="true">
          <circle cx="25" cy="25" r="23" fill="none" stroke="#2a2a2a" stroke-width="2"/>
          <path d="M18 13 c-3 1 -5 4 -4 8 c2 7 8 13 15 15 c4 1 7 -1 8 -4 l-5 -4 c-1 -1 -2 -1 -3 0 l-2 2 c-3 -1 -6 -4 -7 -7 l2 -2 c1 -1 1 -2 0 -3 z" fill="#2a2a2a"/>
        </svg>
        <div>001 482 615 390<br>001 482 615 390</div>
      </div>
      <div class="contact-box address">
        <svg class="contact-icon" viewBox="0 0 50 50" aria-hidden="true">
          <circle cx="25" cy="25" r="23" fill="none" stroke="#2a2a2a" stroke-width="2"/>
          <path d="M25 11 c-6 0 -10 4 -10 10 c0 7 10 18 10 18 s10 -11 10 -18 c0 -6 -4 -10 -10 -10 z" fill="#2a2a2a"/>
          <circle cx="25" cy="21" r="4" fill="#d2d2d2"/>
        </svg>
        <div>Elm Court St.2210<br>Lorem City. Halden</div>
      </div>
      <div class="contact-box web">
        <svg class="contact-icon" viewBox="0 0 50 50" aria-hidden="true">
          <circle cx="25" cy="25" r="23" fill="none" stroke="#2a2a2a" stroke-width="2"/>
          <circle cx="25" cy="25" r="14" fill="none" stroke="#2a2a2a" stroke-width="2"/>
          <ellipse cx="25" cy="25" rx="6" ry="14" fill="none" stroke="#2a2a2a" stroke-width="2"/>
          <line x1="11" y1="25" x2="39" y2="25" stroke="#2a2a2a" stroke-width="2"/>
          <line x1="13" y1="18" x2="37" y2="18" stroke="#2a2a2a" stroke-width="1.6"/>
          <line x1="13" y1="32" x2="37" y2="32" stroke="#2a2a2a" stroke-width="1.6"/>
        </svg>
        <div>info@dalvinsoeurs.com<br>www.dalvinsoeurs.com</div>
      </div>
    </section>
  </article>
</main>
</body>
</html>
```